website re-design - the brisk loft

The Brisk Loft is an existing website that we built using a new zealand based online CMS tool which is quite flexible and accomodates custom designs. You can check it here: http://www.pagecrafter.co.nz/.

We have a logo already and the content on the website is OK.
The website can be found at www.thebriskloft.com.au

mainly the homepage, but if the design is easily adapted to the other pages then, we will commission the winner to update these pages also.
Updates

Hi there,  I am uploading an image to be used as the main image on the homepage design,  so all submissions have the same image.

Target Market(s)

property developers, architects, builders, home buyers

Industry/Entity Type

Shop

Requirements
Must have
• Must utilise the existing CMS or at least be compatible to upload
Nice to have
• a promotional banner that can be turned off and on and changed as required as we offer different promotions over time.

```html
<!DOCTYPE html>
<html lang="en">
<head>
<meta charset="utf-8">
<title>The Brisk Loft — Architectural Scale Models</title>
<link rel="stylesheet" href="https://fonts.googleapis.com/css2?family=Montserrat:wght@400;500;600&family=Arimo:wght@400;700&display=swap">
<style>
:root{
  --orange:#e8731a;
  --amber:#f5b01c;
  --green:#6aaf1e;
  --blue:#2aa3d8;
  --ink:#222;
  --text:#555;
  --muted:#8a8a8a;
  --rule:#c9c9c9;
  --nav:#1b1b1b;
  --btn:#9a9a9a;
  --white:#fff;
}
*{box-sizing:border-box;margin:0;padding:0}
html,body{width:904px;height:1200px;overflow:hidden;background:var(--white)}
body{position:relative;font-family:"Arimo",Arial,sans-serif;color:var(--text)}
.abs{position:absolute}
a{color:inherit;text-decoration:none}

/* header */
.brand{left:24px;top:16px;display:flex;align-items:center;gap:14px}
.brand-mark{width:128px;height:74px;background:var(--orange)}
.brand-name{font-family:"Montserrat",sans-serif;font-weight:500;font-size:27px;color:#3a3a3a;letter-spacing:.2px;line-height:1}
.brand-tag{font-family:"Montserrat",sans-serif;font-weight:500;font-size:13px;color:var(--orange);margin-top:3px;letter-spacing:.3px}
.utility{right:26px;top:13px;font-size:11px;color:var(--orange)}
.utility span{color:var(--muted);margin:0 3px}
.phone{right:30px;top:45px;display:flex;align-items:center;gap:8px;font-family:"Montserrat",sans-serif;font-size:19px;color:#444}
.phone em{font-style:normal;color:var(--orange)}

.header-band{left:0;top:98px;width:904px;height:30px;background:linear-gradient(#fafafa,#e6e6e6);border-top:1px solid #ddd}
.main-nav{left:152px;top:97px;width:601px;height:32px;display:flex;background:repeating-linear-gradient(135deg,#222 0 2px,#121212 2px 4px);box-shadow:0 2px 3px rgba(0,0,0,.3);padding-left:39px}
.main-nav a{font-family:"Montserrat",sans-serif;font-size:14px;color:var(--white);line-height:32px;padding:0 20px 0 16px}
.main-nav a.current{background:var(--orange);width:93px;text-align:center;padding:0}

/* hero */
.hero{left:28px;top:137px;width:848px;height:316px;background:linear-gradient(160deg,#b9b4bb 0%,#6f7d6a 35%,#8d8a8f 60%,#c9c3c2 100%);box-shadow:0 10px 12px -8px rgba(0,0,0,.45)}
.hero-caption{left:0;bottom:0;width:100%;height:42px;background:rgba(25,25,25,.78);color:var(--white);font-family:"Montserrat",sans-serif;font-size:13.5px;line-height:42px;text-align:center;padding-right:40px}
.hero-dots{right:26px;top:15px;display:flex;gap:4px}
.hero-dots i{width:11px;height:11px;border-radius:50%;background:#ddd}
.hero-dots i.on{background:var(--orange)}

.rule{height:1px;background:var(--rule)}

/* features */
.feature{top:482px;width:208px;height:140px}
.feature-head{position:absolute;left:0;top:17px;width:100%;height:27px;color:var(--white);font-family:"Montserrat",sans-serif;font-weight:600;font-size:17px;line-height:27px;padding-left:54px}
.feature-icon{position:absolute;left:2px;top:0;width:42px;height:44px;border-radius:4px}
.feature p{position:absolute;left:4px;top:55px;width:200px;font-size:11px;line-height:16.5px;color:#666}
.more{position:absolute;font-size:11.5px;color:var(--orange)}
.feature .more{right:14px;top:114px}
.vsep{width:1px;background:var(--rule)}

/* welcome */
h2{font-family:"Montserrat",sans-serif;font-weight:500;font-size:17.5px;color:var(--ink)}
.lead{left:26px;top:679px;width:580px;font-size:13px;line-height:17px;color:#111}
.body-copy{left:26px;top:724px;width:580px;font-size:11px;line-height:16.5px;color:#666}
.subhead{left:26px;top:815px;font-size:13px;color:#111}
.steps{left:46px;top:844px;list-style:none;font-size:11px;color:#555}
.steps li{height:27px;position:relative;padding-left:25px}
.steps li::before{content:"»";position:absolute;left:0;top:-3px;color:var(--orange);font-size:14px;font-weight:700}
.btn{display:block;background:var(--btn);color:var(--white);font-size:11.5px;text-align:center}

/* news */
.thumb{border:1px solid #ddd;padding:4px;background:var(--white)}
.thumb div{width:100%;height:100%}
.date{background:var(--orange);color:var(--white);font-size:11px;font-style:italic;font-weight:700;line-height:19px;text-align:center}
.news-text{font-size:11px;line-height:16.5px;color:#555;width:165px}

/* sidebar */
.service-title{left:630px;top:798px;font-size:13px;font-weight:700;color:var(--orange)}
.service-sub{left:630px;top:816px;font-size:12px;color:#111}
.service-copy{left:630px;top:839px;width:250px;font-size:11px;line-height:16.5px;color:#555}

/* footer */
.footer-nav{left:0;top:1135px;width:904px;text-align:center;font-family:"Montserrat",sans-serif;font-size:11px;color:#222;padding-right:4px}
.footer-nav span{margin:0 3px}
.copyright{left:0;top:1162px;width:904px;text-align:center;font-family:"Montserrat",sans-serif;font-size:11px;color:#222}
.connect{left:780px;top:1135px;font-family:"Montserrat",sans-serif;font-size:11px;color:#222}
.social{top:1155px;width:24px;height:24px;border-radius:4px}
</style>
</head>
<body>

<header>
  <div class="abs brand">
    <div class="brand-mark" aria-hidden="true"></div>
    <div>
      <div class="brand-name">THE BRISK LOFT</div>
      <div class="brand-tag">ARCHITECTURAL SCALE MODELS</div>
    </div>
  </div>
  <div class="abs utility"><a href="#">Order online</a><span>|</span><a href="#">Get a Quote</a><span>|</span><a href="#">Sitmap</a></div>
  <div class="abs phone">
    <svg width="22" height="20" viewBox="0 0 22 20" aria-hidden="true"><path d="M1 7c0-4 4-6 10-6s10 2 10 6l-4 1-1-3H6L5 8z" fill="#111"/><path d="M6 8h10l4 5v6H2v-6z" fill="#111"/><circle cx="11" cy="14" r="2.6" fill="#fff"/></svg>
    <span><em>(08)</em> 5550 0147</span>
  </div>
  <div class="abs header-band"></div>
  <nav class="abs main-nav">
    <a class="current" href="#">Home</a>
    <a href="#">About Us</a>
    <a href="#">Gallery</a>
    <a href="#">3d visualisation</a>
    <a href="#">Contact</a>
  </nav>
</header>

<section class="abs hero" role="img" aria-label="Photograph of an architectural scale model of a housing development with rows of white buildings and trees">
  <div class="abs hero-caption">" a picture's worth a thousand words... a model says it all..."</div>
  <div class="abs hero-dots" style="top:auto;bottom:12px"><i></i><i class="on"></i><i></i><i></i><i></i></div>
</section>

<div class="abs rule" style="left:20px;top:480px;width:860px"></div>

<section>
  <div class="abs feature" style="left:20px">
    <div class="feature-head" style="background:var(--orange)">Planning</div>
    <div class="feature-icon" role="img" aria-label="Light bulb icon" style="background:radial-gradient(circle at 50% 40%,#ffe34d,#f0a818)"></div>
    <p>It was popularised in the 1960s with the release of Letraset sheets containing Lorem Ipsum passages.</p>
    <a class="more" href="#">more info »</a>
  </div>
  <div class="abs vsep" style="left:233px;top:490px;height:130px"></div>
  <div class="abs feature" style="left:238px">
    <div class="feature-head" style="background:var(--amber)">Analysis</div>
    <div class="feature-icon" role="img" aria-label="Circular arrows icon" style="background:radial-gradient(circle,#7fd1e8,#2a8fb0);border-radius:50%"></div>
    <p>It was popularised in the 1960s with the release of Letraset sheets containing Lorem Ipsum passages.</p>
    <a class="more" href="#">more info »</a>
  </div>
  <div class="abs vsep" style="left:452px;top:490px;height:130px"></div>
  <div class="abs feature" style="left:457px;width:209px">
    <div class="feature-head" style="background:var(--green)">Strategy</div>
    <div class="feature-icon" role="img" aria-label="Bar chart icon" style="background:linear-gradient(90deg,#e8731a,#f5b01c,#6aaf1e)"></div>
    <p>It was popularised in the 1960s with the release of Letraset sheets containing Lorem Ipsum passages.</p>
    <a class="more" href="#">more info »</a>
  </div>
  <div class="abs vsep" style="left:670px;top:490px;height:130px"></div>
  <div class="abs feature" style="left:673px;width:210px">
    <div class="feature-head" style="background:var(--blue)">Technologies</div>
    <div class="feature-icon" role="img" aria-label="Stacked devices icon" style="background:linear-gradient(#c33,#888)"></div>
    <p>It was popularised in the 1960s with the release of Letraset sheets containing Lorem Ipsum passages.</p>
    <a class="more" href="#" style="right:14px">more info »</a>
  </div>
</section>

<div class="abs rule" style="left:20px;top:628px;width:860px"></div>

<main>
  <h2 class="abs" style="left:31px;top:647px">Welcome To Our Site</h2>
  <p class="abs lead">Getting an architectural model produced can be expensive and time consuming, but it can also add a lot of value to a project.</p>
  <p class="abs body-copy">There are many variations of passages of Lorem Ipsum available, but the majority have suffered alteration in some form, by injected humour, or randomised words which don't look even slightly believable. If you are going to use a passage of Lorem Ipsum, you need to be sure there isn't anything embarrassing hidden in the middle of text. All the Lorem Ipsum generators on the Internet tend to repeat predefined chunks as necessary, making this the first true generator on the Internet.</p>
  <p class="abs subhead">It's this easy</p>
  <ul class="abs steps">
    <li>Order online or fill in the quote form.</li>
    <li>We'll build your model and deliver it right to your door.</li>
  </ul>
  <a class="abs btn" href="#" style="left:514px;top:893px;width:78px;height:26px;line-height:26px">more info</a>

  <div class="abs rule" style="left:32px;top:936px;width:553px"></div>
  <h2 class="abs" style="left:31px;top:953px">What’s new?</h2>

  <div class="abs thumb" style="left:22px;top:990px;width:100px;height:87px"><div role="img" aria-label="Model of a white multi-storey house on a green base" style="background:linear-gradient(#e9ecef,#cfd4d0 60%,#7fae58)"></div></div>
  <div class="abs date" style="left:131px;top:994px;width:72px">Nov 28,2011</div>
  <p class="abs news-text" style="left:128px;top:1021px">Getting an architectural model produced can be expensive and time consuming.</p>

  <div class="abs thumb" style="left:320px;top:990px;width:100px;height:87px"><div role="img" aria-label="Cutaway 3D rendering of a house interior" style="background:linear-gradient(135deg,#b9a58a,#eee 55%,#ddd)"></div></div>
  <div class="abs date" style="left:429px;top:994px;width:72px">Nov 28,2011</div>
  <p class="abs news-text" style="left:427px;top:1021px">Getting an architectural model produced can be expensive and time consuming.</p>
</main>

<div class="abs vsep" style="left:607px;top:645px;height:445px"></div>

<aside>
  <h2 class="abs" style="left:621px;top:647px">Our Services</h2>
  <div class="abs thumb" style="left:647px;top:681px;width:204px;height:78px"><div role="img" aria-label="3D rendering of a two-storey house with brown roof" style="background:linear-gradient(#bcd9f0,#e3e3e3 45%,#8d8579)"></div></div>
  <p class="abs service-title">consectetuer adipis</p>
  <p class="abs service-sub">Cing elit. Praesent vestibulum molestie lacus.</p>
  <p class="abs service-copy">All the Lorem Ipsum generators on the Internet tend to repeat predefined chunks as necessary, making this the first true generator on the Internet.</p>
  <div class="abs rule" style="left:622px;top:903px;width:253px"></div>
  <h2 class="abs" style="left:621px;top:920px">Testimonials</h2>
  <div class="abs thumb" style="left:618px;top:957px;width:101px;height:108px"><div role="img" aria-label="Portrait photo of the client giving the testimonial" style="background:linear-gradient(#f2f2f2,#d9c3b0 55%,#2a2f3a)"></div></div>
  <div class="abs date" style="left:727px;top:958px;width:73px">Nov 28,2011</div>
  <p class="abs" style="left:727px;top:985px;font-size:12px;color:#111">Daniel</p>
  <p class="abs news-text" style="left:725px;top:1004px;width:160px">Getting an architectural model produced can be expensive and time consuming.</p>
  <a class="abs btn" href="#" style="left:799px;top:1064px;width:79px;height:26px;line-height:26px">more info</a>
</aside>

<footer>
  <div class="abs rule" style="left:20px;top:1116px;width:864px"></div>
  <nav class="abs footer-nav"><a href="#">Home</a><span>|</span><a href="#">About Us</a><span>|</span><a href="#">Gallery</a><span>|</span><a href="#">3d visualisation</a><span>|</span><a href="#">Contact</a></nav>
  <p class="abs copyright">2011 ©&nbsp; Copyrights.thebriskloft.Receive</p>
  <p class="abs connect">Connect with us</p>
  <span class="abs social" style="left:779px;background:#3b5a9a"></span>
  <span class="abs social" style="left:811px;background:#4fb2e0"></span>
  <span class="abs social" style="left:843px;background:#e8731a"></span>
</footer>

</body>
</html>
```